Poster Design Project

Need a design for a music festival called Counter-Lanternweek

The design needs to have areas for the following:
- Band Names
- DJ Names
- Sponsor Names and Logos
- Event location, Date & Time

Industry/Entity Type

Festival

```html
<!DOCTYPE html>
<html lang="en">
<head>
<meta charset="utf-8">
<title>Counter-Lanternweek</title>
<link href="https://fonts.googleapis.com/css2?family=Anton&family=Oswald:wght@500;700&family=Permanent+Marker&display=swap" rel="stylesheet">
<style>
  :root {
    --bg-dark: #2e2e2e;
    --bg-mid: #5a5a5a;
    --bg-light: #cfcfcf;
    --ink-white: #ffffff;
    --ink-dark: #3c3c3c;
    --accent-red: #e3231f;
  }
  html, body {
    margin: 0;
    padding: 0;
    width: 816px;
    height: 1200px;
    overflow: hidden;
    background: var(--bg-dark);
  }
  .poster {
    position: relative;
    width: 816px;
    height: 1200px;
    overflow: hidden;
    background:
      radial-gradient(ellipse 420px 520px at 50% 42%, var(--bg-light) 0%, #9a9a9a 35%, var(--bg-mid) 65%, var(--bg-dark) 100%);
    font-family: "Oswald", "Arial Narrow", sans-serif;
    text-align: center;
    color: var(--ink-white);
  }
  .wings-art {
    position: absolute;
    left: 40px;
    top: 150px;
    width: 736px;
    height: 380px;
  }
  .cable-art {
    position: absolute;
    top: 560px;
    width: 150px;
    height: 260px;
  }
  .cable-art--left { left: 0; }
  .cable-art--right { right: 0; }
  .title {
    position: absolute;
    left: 0;
    right: 0;
    top: 30px;
    margin: 0;
    font-family: "Anton", "Impact", sans-serif;
    font-weight: 400;
    font-size: 200px;
    line-height: 0.86;
    letter-spacing: 4px;
    color: var(--ink-dark);
  }
  .title-line { display: block; }
  .title-overlay {
    position: absolute;
    left: 0;
    right: 0;
    top: 250px;
    font-family: "Permanent Marker", cursive;
    font-size: 118px;
    line-height: 1;
    color: var(--accent-red);
    transform: rotate(-8deg);
  }
  .event-date {
    position: absolute;
    left: 0; right: 0;
    top: 686px;
    margin: 0;
    font-weight: 700;
    font-size: 38px;
    color: var(--accent-red);
    letter-spacing: 1px;
  }
  .lineup-heading {
    position: absolute;
    left: 0; right: 0;
    top: 738px;
    margin: 0;
    font-weight: 700;
    font-size: 30px;
    line-height: 1;
  }
  .lineup {
    position: absolute;
    left: 0; right: 0;
    top: 776px;
    margin: 0;
    padding: 0;
    list-style: none;
    font-weight: 700;
    font-size: 30px;
    line-height: 31px;
    text-transform: uppercase;
  }
  .sponsor-heading {
    position: absolute;
    left: 0; right: 0;
    top: 962px;
    margin: 0;
    font-weight: 700;
    font-size: 46px;
    line-height: 1;
    color: var(--accent-red);
  }
  .sponsor-mark {
    position: absolute;
    left: 0; right: 0;
    top: 1022px;
    display: flex;
    justify-content: center;
    align-items: center;
    gap: 10px;
    font-weight: 700;
    font-size: 26px;
    line-height: 1;
  }
  .sponsor-mark__square {
    width: 28px;
    height: 28px;
    background: var(--ink-white);
  }
  .sponsor-list {
    position: absolute;
    left: 0; right: 0;
    top: 1062px;
    margin: 0;
    font-weight: 700;
    font-size: 17px;
    line-height: 1;
  }
  .more-info {
    position: absolute;
    left: 0; right: 0;
    top: 1084px;
    margin: 0;
    font-weight: 700;
    font-size: 17px;
    line-height: 1;
  }
  .social-handle {
    position: absolute;
    left: 0; right: 0;
    top: 1104px;
    display: flex;
    justify-content: center;
    align-items: center;
    gap: 6px;
    font-weight: 700;
    font-size: 17px;
    line-height: 1;
  }
  .social-handle__square {
    width: 15px;
    height: 15px;
    background: var(--ink-white);
  }
  .venue-name {
    position: absolute;
    left: 0; right: 0;
    top: 1124px;
    margin: 0;
    font-weight: 700;
    font-size: 44px;
    line-height: 1;
    color: var(--accent-red);
  }
  .venue-address {
    position: absolute;
    left: 0; right: 0;
    top: 1170px;
    margin: 0;
    font-weight: 700;
    font-size: 22px;
    line-height: 1;
  }
</style>
</head>
<body>
  <main class="poster">
    <svg class="wings-art" role="img" aria-label="Pair of spread feathered wings behind the festival title" viewBox="0 0 736 380">
      <defs>
        <radialGradient id="wingGlow" cx="50%" cy="50%" r="50%">
          <stop offset="0%" stop-color="#8a8a8a" stop-opacity="0.55"/>
          <stop offset="100%" stop-color="#8a8a8a" stop-opacity="0"/>
        </radialGradient>
      </defs>
      <ellipse cx="368" cy="190" rx="368" ry="190" fill="url(#wingGlow)"/>
    </svg>

    <svg class="cable-art cable-art--left" role="img" aria-label="Guitar cables reaching in from the left edge" viewBox="0 0 150 260">
      <rect width="150" height="260" fill="#3a3a3a" opacity="0.35"/>
    </svg>
    <svg class="cable-art cable-art--right" role="img" aria-label="Guitar cables reaching in from the right edge" viewBox="0 0 150 260">
      <rect width="150" height="260" fill="#3a3a3a" opacity="0.35"/>
    </svg>

    <h1 class="title">
      <span class="title-line">LAN</span>
      <span class="title-line">TERN</span>
      <span class="title-line">WEEK</span>
    </h1>
    <div class="title-overlay">COUNTER</div>

    <p class="event-date">AUGUST 21, 2012 | 11:00A - UNTIL</p>

    <h2 class="lineup-heading">PERFORMING LIVE</h2>
    <ul class="lineup">
      <li>Quiet Harbor</li>
      <li>Odd Theory</li>
      <li>Hale &amp; Wren Company</li>
      <li>The Ironfoxes</li>
      <li>Clara Wendt</li>
      <li>And Many More!</li>
    </ul>

    <h2 class="sponsor-heading">SPONSORED BY</h2>
    <div class="sponsor-mark">
      <span class="sponsor-mark__square"></span>
      <span>MOVEMENT CREW</span>
    </div>
    <p class="sponsor-list">STARLING BREWING COMPANY, AND NORTHSIDE BREWING COMPANY</p>
    <p class="more-info">MORE INFO WWW.MOVEMENTCREW.COM</p>
    <div class="social-handle">
      <span class="social-handle__square"></span>
      <span>/MOVEMENTCREW</span>
    </div>

    <h2 class="venue-name">THE TOOL ROOM</h2>
    <p class="venue-address">412 E. 28TH ST MILLBROOK, NC 28999</p>
  </main>
</body>
</html>
```